Business Card Design

We need a business card design for a new company called Valmere Joinery. We make, design and install all joinery.
We want a classy business card which is not to busy, we want a double sided card with just the logo on one side and all the required information on the other. We are a partnership so would like cards with both names and numbers. We would like to see a design which blends in with our logo and really makes it pop.

Reason: I would like my logo displayed on the business card please.

Industry/Entity Type

Business

Contact Information for Business Card

Name- Paul Varden Phone Number- 048571620
Name- Tom Varden Phone Number- 0417265190 E-mail- valmerejoinery@brindlemail.example
License Number- 853027k Company Name- Valmere Joinery ABN-47 508 293 614

Colors
0456a4
ffffff

```html
<!DOCTYPE html>
<html lang="en">
<head>
<meta charset="utf-8">
<title>Valmere Joinery – Business Card</title>
<link rel="stylesheet" href="https://fonts.googleapis.com/css2?family=Ubuntu:wght@400;500;700&display=swap">
<style>
  :root {
    --brand-blue: #0456a4;
    --paper: #ffffff;
    --ink: #2a2a2c;
    --accent-black: #1b1b1d;
    --backdrop: #e6e8eb;
  }
  * { box-sizing: border-box; margin: 0; padding: 0; }
  html, body {
    width: 1200px;
    height: 1000px;
    overflow: hidden;
    background: var(--backdrop);
    font-family: "Ubuntu", sans-serif;
    color: var(--ink);
  }
  .card {
    position: absolute;
    left: 180px;
    width: 840px;
    height: 470px;
    background: var(--paper);
    box-shadow: 0 6px 18px rgba(0,0,0,0.18);
    overflow: hidden;
  }
  .card--front { top: 15px; }
  .card--back { top: 515px; }

  .brand {
    position: absolute;
    display: flex;
    align-items: center;
    gap: 18px;
  }
  .brand__square {
    width: 58px;
    height: 58px;
    background: var(--brand-blue);
  }
  .brand__name {
    font-size: 46px;
    font-weight: 500;
    color: var(--ink);
    letter-spacing: 1px;
  }
  .card--front .brand { left: 70px; top: 60px; }
  .card--back .brand { left: 90px; top: 150px; }

  .band {
    position: absolute;
    right: 0;
    background: var(--brand-blue);
  }
  .band-tab {
    position: absolute;
    background: var(--accent-black);
  }
  .card--front .band { left: 74px; top: 180px; height: 140px; }
  .card--front .band-tab { left: 52px; top: 180px; width: 18px; height: 140px; }
  .card--back .band { left: 124px; top: 318px; height: 48px; }
  .card--back .band-tab { left: 96px; top: 318px; width: 22px; height: 48px; }

  .partner {
    position: absolute;
    top: 214px;
    color: var(--paper);
  }
  .partner__name { font-size: 28px; font-weight: 700; }
  .partner__phone { font-size: 24px; font-weight: 400; letter-spacing: 1px; margin-top: 4px; }
  .partner--first { left: 112px; }
  .partner--second { left: 470px; }

  .details {
    position: absolute;
    left: 120px;
    top: 344px;
    font-size: 22px;
    line-height: 1.22;
  }
  .details__company { font-weight: 700; font-size: 23px; }
  .details__email { margin-top: 10px; }
  .details__label { color: var(--brand-blue); }

  .website {
    position: absolute;
    left: 160px;
    top: 330px;
    font-size: 22px;
    letter-spacing: 2px;
    color: var(--paper);
  }
</style>
</head>
<body>
  <section class="card card--front" aria-label="Card front">
    <div class="brand">
      <span class="brand__square"></span>
      <span class="brand__name">Valmere Joinery</span>
    </div>
    <div class="band-tab"></div>
    <div class="band"></div>
    <div class="partner partner--first">
      <div class="partner__name">Paul Varden</div>
      <div class="partner__phone">048571620</div>
    </div>
    <div class="partner partner--second">
      <div class="partner__name">Tom Varden</div>
      <div class="partner__phone">0417265190</div>
    </div>
    <div class="details">
      <div class="details__company">Valmere Joinery</div>
      <div>License Number- 853027k</div>
      <div>ABN-47 508 293 614</div>
      <div class="details__email"><span class="details__label">M+</span> valmerejoinery@brindlemail.example</div>
    </div>
  </section>

  <section class="card card--back" aria-label="Card back">
    <div class="brand">
      <span class="brand__square"></span>
      <span class="brand__name">Valmere Joinery</span>
    </div>
    <div class="band-tab"></div>
    <div class="band"></div>
    <div class="website">www.valmerejoinery.example</div>
  </section>
</body>
</html>
```